Brinmore Sports Pub. Where the locals go!!

We are creating a sports pub. We are needing a fun website that offers our menu along with an event page and general info. We have some attached links that we really like:
https://www.dolvetts.example/
https://www.cafemiralto.example/
https://www.quillstonepx.example/
We are doing a pirate theme but that is because the area we are in. We would like to see a pirate like in our logo doing something like drinking real time similar to the dolvetts website above.
Target Market(s)
Sports Fans
Industry/Entity Type
Pub, Bar, Restaurant
Coding
Coded - Design and coding required
Number of Pages Required
3 page
Font styles to use
Other font styles liked:
- see uploads
Look and feel

```html
<!DOCTYPE html>
<html lang="en">
<head>
<meta charset="utf-8">
<title>About – Brinmore Sports Pub</title>
<link rel="stylesheet" href="https://fonts.googleapis.com/css2?family=Montserrat:wght@400;500&family=Roboto:wght@400&family=Smokum&display=swap">
<style>
  :root {
    --bg: #000000;
    --white: #ffffff;
    --gold: #e8cf98;
    --accent: #e39b4b;
    --accent-ink: #2a1a08;
    --rope-light: #b9b9b9;
    --rope-dark: #5a5a5a;
    --body-text: #e9e1d2;
    --photo-warm: #8a4b2a;
    --photo-deep: #2b1712;
    --art-grey: #6e6e6e;
  }
  * { margin: 0; padding: 0; box-sizing: border-box; }
  html, body { width: 1036px; height: 1200px; overflow: hidden; background: var(--bg); }
  body { position: relative; font-family: "Montserrat", sans-serif; color: var(--white); }

  .site-nav { position: absolute; top: 46px; display: flex; align-items: center; font-size: 12px; letter-spacing: 0.2px; }
  .site-nav a { color: var(--white); text-decoration: none; }
  .site-nav a.is-current { color: var(--accent); }
  .site-nav .sep { margin: 0 10px; }
  .site-nav--left { left: 97px; }
  .site-nav--right { left: 641px; }
  .book-button {
    position: absolute; left: 834px; top: 38px; width: 106px; height: 33px;
    background: var(--accent); color: var(--accent-ink); border-radius: 2px;
    font-size: 12px; display: flex; align-items: center; justify-content: center; text-decoration: none;
  }

  .brand-mark {
    position: absolute; width: 182px; height: 182px; left: 427px; border-radius: 50%;
    background: var(--white); border: 4px solid var(--bg); box-shadow: 0 0 0 2px var(--white);
    display: flex; align-items: center; justify-content: center; text-align: center; z-index: 3;
  }
  .brand-mark span { font-family: "Montserrat", sans-serif; font-weight: 500; font-size: 19px; line-height: 1.25; color: var(--bg); width: 130px; }
  .brand-mark--header { top: 31px; }
  .brand-mark--footer { top: 975px; }

  .rope-band { position: absolute; left: 0; width: 1036px; height: 9px;
    background: linear-gradient(180deg, var(--rope-dark), var(--rope-light) 50%, var(--rope-dark)); }
  .rope-band--hero-top { top: 101px; }
  .rope-band--hero-bottom { top: 422px; }
  .rope-band--footer { top: 930px; }

  .hero-photo { position: absolute; top: 110px; left: 0; width: 1036px; height: 312px;
    background: linear-gradient(180deg, #5a3426 0%, var(--photo-warm) 55%, var(--photo-deep) 100%); }
  .hero-photo::before, .hero-photo::after { content: ""; position: absolute; top: 0; width: 96px; height: 100%; background: rgba(0,0,0,0.25); }
  .hero-photo::before { left: 0; }
  .hero-photo::after { right: 0; }

  .about { position: absolute; left: 97px; top: 500px; width: 415px; }
  .about h1 { font-family: "Smokum", serif; font-weight: 400; font-size: 20px; color: var(--gold); letter-spacing: 1px; margin-bottom: 18px; }
  .about p { font-family: "Roboto", sans-serif; font-size: 15px; line-height: 22.2px; color: var(--body-text); margin-bottom: 22px; }

  .about-art { position: absolute; left: 628px; top: 512px; width: 408px; height: 252px;
    background: radial-gradient(ellipse at 50% 55%, #3c3c3c 0%, #1c1c1c 55%, var(--bg) 80%); }

  .footer-links { position: absolute; left: 96px; top: 1041px; font-size: 12px; line-height: 22px; color: var(--gold); }
  .footer-links a { color: var(--gold); text-decoration: none; }
  .footer-links .sep { margin: 0 12px; }
  .footer-legal { position: absolute; left: 698px; top: 1038px; font-size: 14px; line-height: 22px; color: var(--gold); }
</style>
</head>
<body>
  <nav class="site-nav site-nav--left">
    <a href="#">HOURS &amp; LOCATION</a><span class="sep">|</span>
    <a href="#" class="is-current">ABOUT</a><span class="sep">|</span>
    <a href="#">PRESS</a>
  </nav>
  <nav class="site-nav site-nav--right">
    <a href="#">MENUS</a><span class="sep">|</span>
    <a href="#">PRIVATE EVENTS</a>
  </nav>
  <a href="#" class="book-button">Book Now</a>

  <div class="brand-mark brand-mark--header"><span>Brinmore Sports Pub</span></div>

  <div class="rope-band rope-band--hero-top"></div>
  <div class="hero-photo" role="img" aria-label="Pub interior with tufted leather booths, brick wall and framed pictures"></div>
  <div class="rope-band rope-band--hero-bottom"></div>

  <section class="about">
    <h1>ABOUT US:</h1>
    <p>Lorem Ipsum is simply dummy text of the printing and typesetting industry. Lorem Ipsum has been the industry's standard dummy text ever since the 1500s,</p>
    <p>when an unknown printer took a galley of type and scrambled it to make a type specimen book. It has survived not only five centuries,Lorem Ipsum is simply dummy text of the printing and typesetting industry. Lorem Ipsum has been the industry's standard dummy text ever since the 1500s,</p>
    <p>when an unknown printer took a galley of type and scrambled it to make a type specimen book. It has survived not only five centuries,</p>
  </section>

  <div class="about-art" role="img" aria-label="Grey illustration of a pirate holding a beer mug beside a sailing ship"></div>

  <div class="rope-band rope-band--footer"></div>

  <footer>
    <div class="footer-links">
      <a href="#">HOURS &amp; LOCATION</a><span class="sep">|</span><a href="#">ABOUT</a><span class="sep">|</span><a href="#">PRESS</a><br>
      <a href="#">MENUS</a><span class="sep">|</span><a href="#">PRIVATE EVENTS</a>
    </div>
    <div class="brand-mark brand-mark--footer"><span>Brinmore Sports Pub</span></div>
    <p class="footer-legal">Brinmore Sports Pub ©<br>Copyright 2023. All Rights Reserved.</p>
  </footer>
</body>
</html>
```